Create a packaging design for a new deodorant

New product container label. The jar is 2.75" in diameter and 2.75" high. The (transparent) label size is 1.5" by 8.5" and will wrap nearly fully around the jar when applied. Approximately 3.25" of the label will be devoted to the name and front section of the jar (what I am requesting you to design). Remaining part of the label will include a brief description, directions, general warning, ingredients, manufacturer, distributor, and barcode. The deodorant name is TOV. It is a clear colorless solution, ecologically friendly, naturally occurring deodorant salt solution. Water based, no alcohol, non-sticky, non-waxy, non-staining, just simple, clean and effective. Nature's way of getting the job done. Label to use transparent green and/or blue colors. Phrases such as " Fresh as a Springtime shower" or "Fresh as an ocean breeze" might be used. The deodorant has a NEW, unique, revolutionary applicator.

Target Market(s)

All adult men and women

Industry/Entity Type

Product

Number of Pages Required

1 page

Requirements
Nice to have
• TOV
• This is a new deodorant, a simple but elegant solution to an age-old problem.
• Why I Hate Deodorants
• I’ve had my share of problems with deodorants, and with antiperspirants for that matter, too. First off, the last thing I want to do when I step out of the shower is to put some sticky, slimy, or waxy goop on clean skin. I don’t like it when it feels like skin sticks together in skin folds. When I used to use the old stick deodorants, I would periodically scrape the edge of the plastic container against my skin and cause an abrasion that would then be irritated for the next 3 days. This would be particularly true when I got down to the bottom of the stick and the medication surface flattened out in the dispenser. Sometimes the deodorant or antiperspirant itself would cause such abrasions to grow red and angry and force me to stop using it altogether for the next week. Then I’d be hunting (and hurting) for alternatives. So every few months I would spend lots of time in the store looking at all the different brands of deodorants to find something that was a bit different - less caustic, less sticky, less stinky, or in a different dispenser that might work better for me. Roll-on deodorants work for me until they don’t. Half the time I’m trying to hold the bottle upside down and squeezing it so the product comes out. The other half of the time the roller ball gets stuck and I’m trying to get it to turn. What a waste of time. Or if it pours out, I have to spread it all over the place to get it thin enough to dry out. I dispensed with antiperspirants years ago when I had to throw away some of my favorite shirts because of sweat (really antiperspirant chemical) stains. I’ve also seen enough people with hidradenitis (infected sweat glands from using some antiperspirants) to know that some of these products that clog skin pores can be serious skin irritants.
• I’m a Natural Kind of Guy
• Don’t get me wrong. I’m not a tree hugger. I haven’t been out on the high seas in a rowboat maneuvering between a harpooner and a whale. But by the same token I don’t buy 3-step hair treatments. I don’t color my hair either. I don’t lounge around in bubble baths. And I don’t like to use heavy-scented cleansers, shampoos or skin products. I’m just looking for something clean, plain and simple ...something that works, that’s safe and dependable. Maybe even a natural product that has a long track record of safety and effectiveness.
• Just try it.....(There’s nothing more we’ll need to say!!)
• TOV uses a natural mineral salt, water, and a preservative. Nothing more. TOV has a unique and patented dispenser. The dispenser was made for the product and made for the job. One swipe application and you’re done! YOU can control the amount of deodorant applied by the sponge applicator. TOV is WATER-BASED. NO ALCOHOL. NO CHEMICALS. NO IRRITANTS. It dries quickly. No drips like you can get from spray bottles. The applicator doesn’t clog up or stop rolling. And it NEVER stains clothing. It’s just simple...easy...effective. And with a simple product we don’t have to charge a lot of money for it. So it’s inexpensive, too. I know you’re going to like this product.
• Swipe it on.... Odor gone!

```html
<!DOCTYPE html>
<html lang="en">
<head>
<meta charset="utf-8">
<title>TOV Deodorant – Jar Label</title>
<link rel="stylesheet" href="https://fonts.googleapis.com/css2?family=Open+Sans:wght@400;600;700&display=swap">
<style>
  :root {
    --page-bg: #ffffff;
    --lid-light: #86c325;
    --lid-mid: #4cb936;
    --lid-dark: #14a040;
    --band-green: #2fae47;
    --text-green: #2a9d3f;
    --silver-edge: #a9a9a9;
    --silver-mid: #d9d9d9;
    --silver-light: #ffffff;
    --shadow: #bdbdbd;
    --band-text: #ffffff;
  }
  html, body {
    margin: 0;
    padding: 0;
    width: 1200px;
    height: 887px;
    overflow: hidden;
    background: var(--page-bg);
  }
  .canvas {
    position: relative;
    width: 1200px;
    height: 887px;
  }
  .jar {
    position: absolute;
    left: 0;
    top: 0;
  }
  .tagline,
  .brand-name,
  .product-type,
  .claims {
    font-family: "Open Sans", Arial, sans-serif;
  }
  .tagline {
    font-weight: 700;
    font-size: 15px;
    letter-spacing: 0.6px;
    fill: var(--text-green);
  }
  .brand-name {
    font-weight: 700;
    font-size: 62px;
    letter-spacing: 4px;
    fill: var(--text-green);
  }
  .product-type {
    font-weight: 400;
    font-size: 15px;
    letter-spacing: 8px;
    fill: var(--text-green);
  }
  .claims {
    font-weight: 400;
    font-size: 10.5px;
    letter-spacing: 0.2px;
    fill: var(--band-text);
  }
</style>
</head>
<body>
<main class="canvas">
  <svg class="jar" width="1200" height="887" viewBox="0 0 1200 887" xmlns="http://www.w3.org/2000/svg" aria-label="TOV deodorant jar">
    <defs>
      <radialGradient id="lid-gradient" cx="600" cy="270" r="300" gradientUnits="userSpaceOnUse">
        <stop offset="0" stop-color="var(--lid-light)"/>
        <stop offset="0.5" stop-color="var(--lid-mid)"/>
        <stop offset="1" stop-color="var(--lid-dark)"/>
      </radialGradient>
      <linearGradient id="silver-gradient" x1="411" y1="0" x2="791" y2="0" gradientUnits="userSpaceOnUse">
        <stop offset="0" stop-color="var(--silver-edge)"/>
        <stop offset="0.25" stop-color="var(--silver-mid)"/>
        <stop offset="0.5" stop-color="var(--silver-light)"/>
        <stop offset="0.75" stop-color="var(--silver-mid)"/>
        <stop offset="1" stop-color="var(--silver-edge)"/>
      </linearGradient>
    </defs>

    <ellipse class="jar-shadow" cx="603" cy="631" rx="196" ry="3.5" fill="var(--shadow)"/>

    <path class="jar-body" d="M411 421 H791 V607 Q791 631 767 631 H435 Q411 631 411 607 Z" fill="url(#silver-gradient)"/>

    <path class="jar-lid" d="M411 421 V287 Q411 253 445 253 H757 Q791 253 791 287 V421 Z" fill="url(#lid-gradient)"/>

    <rect class="claims-band" x="411" y="579" width="380" height="23" fill="var(--band-green)"/>

    <text class="tagline" x="601" y="443" text-anchor="middle">FRESH AS A SPRING SHOWER</text>

    <text class="brand-name" x="603" y="522" text-anchor="middle">TOV</text>

    <text class="product-type" x="604" y="568" text-anchor="middle">DEODORANT</text>

    <text class="claims" x="601" y="594" text-anchor="middle">WATER-BASED. NO ALCOHOL. NO CHEMICALS. NO IRRITANTS</text>
  </svg>
</main>
</body>
</html>
```